Holistic Therapy (aromatherapy, massage, reflexology, life coaching, soul healing, aura reading)

I work for myself as a holistic therapist doing: aromatherapy massage, massage, reflexology, abdominal-sacral massage, life coaching, soul healing, aura readings. I want a business card that doesn't focus on any one of these( so not just feet or a massage couch,but rather a card that creates the feeling of wholeness, healing, health and which can encompass all my therapies - e.g. green or purple are colours I like (especially green, or maybe green on back and purple on front). It's going to be called Rosa Elwin Therapies. I don't want to list all my therapies on the card in case I add others later.). At some point I will create a website but in this instance I just want to get some cards printed to get 'out there' while I design my website.
Updates

Hi, thanks for all your designs. Can you find a way to include the therapies that I offer within the card, either on the front or back…the therapies I offer are: aromatherapy massage, reflexology, swedish body massage, abdominal-sacral massage, nutrition, soul healing, aura readings. (Maybe have them with a bullet point before each?) I am not sure whether they should be on the front of the card or the back or whether having them would spoil the card but it occurred to me that just having rosa elwin therapies doesn't tell people what therapies I offer, hence the new idea to list them somehow…)

Target Market(s)

Mainly women (middle class probably with disposable incomes).

Industry/Entity Type

Massage

Contact Information for Business Card

Rosa Elwin Therapies, Tel: 07942 586113, email: vitalbloom@mailvane.com, (on back of card I want: Rosalind Elwin BScHons, OKQRB, GPCL.)

Requirements
Nice to have
• A logo for Rosa Elwin Therapies would be good.

```html
<!DOCTYPE html>
<html lang="en">
<head>
<meta charset="utf-8">
<title>Rosa Elwin Therapies – Business Card</title>
<link href="https://fonts.googleapis.com/css2?family=Old+Standard+TT:wght@400;700&display=swap" rel="stylesheet">
<style>
  :root {
    --backdrop: #e6dccb;
    --card-back-green: #27a05a;
    --card-back-green-deep: #1c8447;
    --card-back-green-light: #3cb86e;
    --card-front-purple: #6a2470;
    --card-front-purple-deep: #4f1655;
    --card-front-purple-light: #83348a;
    --flourish-tone: #b98fbd;
    --card-ink: #ffffff;
    --card-ink-soft: #f1e6f2;
  }

  * { box-sizing: border-box; margin: 0; padding: 0; }

  html, body {
    width: 1200px;
    height: 1023px;
    overflow: hidden;
  }

  body {
    background: var(--backdrop);
    font-family: "Old Standard TT", "Times New Roman", serif;
    position: relative;
  }

  .card {
    position: absolute;
    border-radius: 4px;
    box-shadow: 0 10px 28px rgba(60, 40, 20, 0.25);
    color: var(--card-ink);
    text-align: center;
    overflow: hidden;
  }

  /* Back of card */
  .card-back {
    left: 120px;
    top: 90px;
    width: 580px;
    height: 331px;
  }

  .damask-field {
    position: absolute;
    inset: 0;
    background:
      radial-gradient(ellipse at 40% 35%, var(--card-back-green-light) 0%, transparent 60%),
      linear-gradient(160deg, var(--card-back-green) 0%, var(--card-back-green-deep) 100%);
  }

  .back-identity {
    position: absolute;
    left: 0;
    right: 0;
    top: 142px;
  }

  .therapist-name {
    font-size: 27px;
    font-weight: 400;
    letter-spacing: 0.5px;
    line-height: 1.1;
  }

  .therapist-credentials {
    font-size: 14px;
    margin-top: 4px;
    letter-spacing: 0.5px;
  }

  /* Front of card */
  .card-front {
    left: 420px;
    top: 470px;
    width: 660px;
    height: 377px;
    background:
      radial-gradient(ellipse at 55% 30%, var(--card-front-purple-light) 0%, transparent 65%),
      linear-gradient(165deg, var(--card-front-purple) 0%, var(--card-front-purple-deep) 100%);
  }

  .flourish-crest {
    position: absolute;
    left: 185px;
    top: 104px;
    width: 290px;
    height: 100px;
  }

  .business-name {
    position: absolute;
    left: 0;
    right: 0;
    top: 196px;
    font-size: 38px;
    font-weight: 400;
    letter-spacing: 0.3px;
  }

  .contact-list {
    position: absolute;
    left: 0;
    right: 0;
    top: 290px;
    list-style: none;
    font-size: 16px;
    line-height: 23px;
    color: var(--card-ink-soft);
    letter-spacing: 0.4px;
  }
</style>
</head>
<body>

  <section class="card card-back" aria-label="Back of business card">
    <div class="damask-field" role="img" aria-label="Green damask floral pattern"></div>
    <div class="back-identity">
      <h2 class="therapist-name">Rosalind Elwin</h2>
      <p class="therapist-credentials">BScHons, OKQRB, GPCL</p>
    </div>
  </section>

  <section class="card card-front" aria-label="Front of business card">
    <svg class="flourish-crest" viewBox="0 0 290 100" role="img" aria-label="Ornamental floral flourish crest">
      <defs>
        <radialGradient id="crest-glow" cx="50%" cy="85%" r="60%">
          <stop offset="0%" stop-color="var(--flourish-tone)" stop-opacity="0.55"/>
          <stop offset="100%" stop-color="var(--flourish-tone)" stop-opacity="0"/>
        </radialGradient>
      </defs>
      <path d="M0 100 Q145 -20 290 100 Z" fill="url(#crest-glow)"/>
    </svg>

    <h1 class="business-name">Rosa Elwin Therapies</h1>

    <ul class="contact-list">
      <li>ph: 07942 586113</li>
      <li>email: vitalbloom@mailvane.com</li>
    </ul>
  </section>

</body>
</html>
```